40k Ultra High Pressure Waterblasing Ad

We need 1 page flyer ad for our industry's brochure/membership directory.
We're a manufacturer & supplier for the Ultra High Pressure Waterblasting industry.
We'd like the ad to be simple and clean, highlighting some of our parts. Our dedication to our customers and affordable prices.
Some of the parts are Dorvel Mastrick Hoses, Sapphire Nozzles, Rotating Jetlance.

Our website is torvaflux.com

Requirements
Must have
• Dorvel Mastrick 40k Hose
• Sapphire Nozzles
• Rotating Jetlance
• **Update - Would like to incorporate the "iron skein logo w/ bulldog" from uploaded dorvel iron skein hose attachment. Highlighting the hose's features.
Nice to have
• Brief Bullet points or something else highlighting what we sell.
• - Pump replacement parts
• - Sapphire Nozzles
• - Rotating Jetlance
• - Fittings and adapters
• - Safety Gear
• I've uploaded past ads we've used.
Should not have
• Lots of text area

```html
<!DOCTYPE html>
<html lang="en">
<head>
<meta charset="utf-8">
<title>Torvaflux Technologies – UHP Surface Preparation Flyer</title>
<link href="https://fonts.googleapis.com/css2?family=Montserrat:wght@700;800&family=Arimo:ital,wght@0,400;0,700;1,400&display=swap" rel="stylesheet">
<style>
  :root{
    --page:#d9d6d6;
    --navy:#0b3f73;
    --navy-deep:#083462;
    --blue:#1576c9;
    --blue-bright:#27a2e8;
    --sky:#d6eefb;
    --white:#ffffff;
    --ink:#0b3f73;
  }
  *{margin:0;padding:0;box-sizing:border-box}
  html,body{width:1200px;height:2400px;overflow:hidden;background:var(--page)}
  .flyer{
    position:absolute;left:100px;top:553px;width:1000px;height:1294px;
    background:var(--white);overflow:hidden;
    box-shadow:0 18px 40px rgba(0,0,0,.28);
    font-family:"Arimo",Arial,sans-serif;
  }
  .flyer-art{position:absolute;inset:0;width:1000px;height:1294px}
  .headline{
    position:absolute;left:81px;top:76px;width:520px;
    font-family:"Montserrat",Arial,sans-serif;font-weight:800;
    font-size:45px;line-height:62px;color:var(--white);letter-spacing:.5px;
  }
  .tagline-family{
    position:absolute;left:81px;top:466px;
    font-weight:700;font-size:25px;line-height:33px;color:var(--white);
  }
  .offer-title{
    position:absolute;left:81px;top:686px;
    font-weight:700;font-size:25px;color:var(--ink);letter-spacing:.5px;
  }
  .offer-list{position:absolute;left:81px;top:742px;list-style:none}
  .offer-list li{
    font-size:30px;line-height:50px;color:var(--ink);
    padding-left:34px;position:relative;
  }
  .offer-list li::before{
    content:"";position:absolute;left:2px;top:15px;
    border-left:13px solid var(--ink);border-top:10px solid transparent;border-bottom:10px solid transparent;
  }
  .motto{
    position:absolute;left:81px;top:1027px;
    font-style:italic;font-size:23px;color:var(--white);
  }
  .brand-name{
    position:absolute;left:600px;top:915px;width:250px;text-align:center;
    font-weight:700;font-size:25px;line-height:30px;color:var(--navy);
  }
  .partner{
    position:absolute;top:1155px;height:66px;background:var(--white);
    display:flex;align-items:center;justify-content:center;
    font-weight:700;font-size:24px;color:var(--navy);
  }
  .partner--dorvel{left:198px;width:112px}
  .partner--skein{left:322px;width:237px}
  .contact{position:absolute;left:596px;top:1140px;color:var(--white)}
  .contact-email{font-size:28px;line-height:40px}
  .contact-phone{font-weight:700;font-size:37px;line-height:48px}
  .contact-web{font-size:26px;line-height:38px}
</style>
</head>
<body>
<main class="flyer">
  <svg class="flyer-art" viewBox="0 0 394 510" preserveAspectRatio="none" aria-hidden="false">
    <defs>
      <linearGradient id="topBand" x1="0" y1="0" x2="1" y2="1">
        <stop offset="0" stop-color="#1e88d8"/>
        <stop offset="1" stop-color="#0d5ba8"/>
      </linearGradient>
      <linearGradient id="lightStripe" x1="0" y1="0" x2="1" y2="0">
        <stop offset="0" stop-color="#2aa6ea"/>
        <stop offset="1" stop-color="#8fd1f5"/>
      </linearGradient>
      <linearGradient id="mottoStripe" x1="0" y1="0" x2="1" y2="0">
        <stop offset="0" stop-color="#1d8fe0"/>
        <stop offset=".7" stop-color="#2aa6ea"/>
        <stop offset="1" stop-color="#ffffff"/>
      </linearGradient>
      <radialGradient id="photoLance" cx=".5" cy=".5" r=".6">
        <stop offset="0" stop-color="#f2f7fb"/><stop offset=".6" stop-color="#b7c3cc"/><stop offset="1" stop-color="#7fc7ef"/>
      </radialGradient>
      <radialGradient id="photoHose" cx=".5" cy=".5" r=".6">
        <stop offset="0" stop-color="#5b6168"/><stop offset=".55" stop-color="#9aa6b0"/><stop offset="1" stop-color="#bfe4f8"/>
      </radialGradient>
      <radialGradient id="photoFittings" cx=".4" cy=".55" r=".6">
        <stop offset="0" stop-color="#c7b9a0"/><stop offset=".6" stop-color="#a9b2b8"/><stop offset="1" stop-color="#c9ebfb"/>
      </radialGradient>
    </defs>

    <!-- top band -->
    <rect class="band-top" x="0" y="0" width="394" height="152" fill="url(#topBand)"/>
    <rect class="band-top-stripe" x="0" y="148" width="394" height="20" fill="url(#lightStripe)"/>
    <!-- family owned band -->
    <rect class="band-family" x="0" y="170" width="270" height="58" fill="var(--navy)"/>
    <!-- right-edge navy panels -->
    <polygon class="edge-panel" points="372,30 394,30 394,420 372,420" fill="var(--navy)"/>
    <!-- motto stripe -->
    <rect class="band-motto" x="0" y="400" width="394" height="22" fill="url(#mottoStripe)"/>
    <!-- footer -->
    <rect class="band-footer" x="0" y="424" width="394" height="86" fill="var(--navy)"/>
    <line class="footer-divider" x1="225" y1="447" x2="225" y2="495" stroke="#ffffff" stroke-width="0.8"/>
    <!-- plain badge -->
    <rect class="badge-origin" x="32" y="445" width="40" height="45" fill="var(--blue-bright)"/>

    <!-- hexagon tiles -->
    <g class="hex hex--lance">
      <polygon points="288,30 358,65 358,145 288,180 218,145 218,65" fill="var(--blue)"/>
      <polygon role="img" aria-label="Photo of a rotating jetlance tool" points="288,38 351,69 351,141 288,172 225,141 225,69" fill="url(#photoLance)"/>
    </g>
    <g class="hex hex--hose">
      <polygon points="218,140 288,175 288,255 218,290 148,255 148,175" fill="var(--blue)"/>
      <polygon role="img" aria-label="Photo of a coiled ultra high pressure hose" points="218,148 281,179 281,251 218,282 155,251 155,179" fill="url(#photoHose)"/>
    </g>
    <g class="hex hex--fittings">
      <polygon points="358,140 428,175 428,255 358,290 288,255 288,175" fill="var(--blue)"/>
      <polygon role="img" aria-label="Photo of brass fittings and adapters" points="358,148 421,179 421,251 358,282 295,251 295,179" fill="url(#photoFittings)"/>
    </g>
    <g class="hex hex--brand">
      <polygon points="288,250 358,285 358,365 288,400 218,365 218,285" fill="var(--blue-bright)"/>
      <polygon points="288,258 351,289 351,361 288,392 225,361 225,289" fill="var(--white)"/>
      <circle cx="288" cy="318" r="13" fill="var(--navy)"/>
    </g>
  </svg>

  <h1 class="headline">SUPPLYING THE ESSENTIALS IN THE UHP SURFACE PREPARATION INDUSTRY</h1>
  <p class="tagline-family">Family Owned<br>and Operated</p>

  <h2 class="offer-title">AT AFFORDABLE PRICES</h2>
  <ul class="offer-list">
    <li>Pump replacement parts</li>
    <li>Sapphire Nozzles</li>
    <li>Rotating Jetlance</li>
    <li>Fittings and adapters</li>
    <li>Safety Gear</li>
  </ul>

  <p class="brand-name">Torvaflux<br>Technologies Inc.</p>

  <p class="motto">“Our Customers Come First”</p>

  <div class="partner partner--dorvel">Dorvel</div>
  <div class="partner partner--skein">Iron Skein</div>

  <address class="contact" style="font-style:normal">
    <p class="contact-email">Email: info@torvaflux.com</p>
    <p class="contact-phone">Call: 555-014-2270</p>
    <p class="contact-web">www.torvaflux.com</p>
  </address>
</main>
</body>
</html>
```